VERIDAX Need a luxury modern business card designed.

Need a luxury modern business card designed. refer to the uploaded files for the company name and logo in the zip file under source files. i will making my descion on monday. so please send in before then so if we need to edit we will have the time. we have a trade show coming up and im on a deadline for printer.

Target Market(s)

high end clients

Contact Information for Business Card

Company nAme and logo. Calvin Ostrow Co-Founder / Project Manager Office # 416-555-0193 Cell # 416-555-0147 VERIDAX.CA Calvin@veridax.ca

Font styles to use
Other font styles liked:
• Modern

Requirements
Must have
• Company name and logo, contact info, using the black, gold and white color scheme.

```html
<!DOCTYPE html>
<html lang="en">
<head>
<meta charset="utf-8">
<title>VERIDAX Business Card</title>
<link href="https://fonts.googleapis.com/css2?family=Lato:wght@300;400;700&display=swap" rel="stylesheet">
<style>
  :root {
    --backdrop: #e4e3e0;
    --card: #353535;
    --gold: #a8975f;
    --white: #ffffff;
    --rule: #5c5c5c;
  }
  * { box-sizing: border-box; margin: 0; padding: 0; }
  html, body {
    width: 1200px; height: 1015px; overflow: hidden;
    background: var(--backdrop);
    font-family: "Lato", sans-serif;
  }
  .sheet {
    width: 1200px; height: 1015px;
    display: flex; flex-direction: column;
    align-items: center; justify-content: center; gap: 40px;
  }
  .card {
    width: 760px; height: 434px;
    background: var(--card);
    border-radius: 4px;
    box-shadow: 0 6px 18px rgba(0,0,0,.18);
    position: relative;
    color: var(--white);
  }
  .brand {
    display: flex; align-items: center; gap: 14px;
  }
  .brand-mark {
    width: 16px; height: 16px; background: var(--gold);
  }
  .brand-name {
    font-weight: 300; letter-spacing: 10px;
    color: var(--white);
  }
  .card-front {
    display: flex; align-items: center; justify-content: center;
  }
  .card-front .brand-name { font-size: 52px; }
  .card-back {
    display: grid; grid-template-columns: 400px 1px 1fr; align-items: center;
  }
  .card-back .brand { justify-content: center; }
  .card-back .brand-name { font-size: 40px; letter-spacing: 8px; }
  .divider { width: 1px; height: 190px; background: var(--rule); }
  .contact { padding-left: 30px; }
  .contact-name {
    color: var(--gold); font-weight: 700; font-size: 22px;
    letter-spacing: 0.5px; text-transform: uppercase;
  }
  .contact-role { font-size: 16px; margin-top: 2px; }
  .contact-list { list-style: none; margin-top: 30px; font-size: 16px; }
  .contact-list li { display: flex; align-items: center; gap: 10px; margin-bottom: 6px; }
  .contact-list svg { width: 15px; height: 15px; flex: none; }
</style>
</head>
<body>
<main class="sheet">
  <section class="card card-front">
    <div class="brand">
      <span class="brand-mark"></span>
      <span class="brand-name">VERIDAX</span>
    </div>
  </section>

  <section class="card card-back">
    <div class="brand">
      <span class="brand-mark"></span>
      <span class="brand-name">VERIDAX</span>
    </div>
    <div class="divider"></div>
    <div class="contact">
      <p class="contact-name">Calvin Ostrow</p>
      <p class="contact-role">Co-Founder / Project Manager</p>
      <ul class="contact-list">
        <li>
          <svg viewBox="0 0 16 16" aria-hidden="true"><path fill="var(--white)" d="M3 2h3l1.5 3.5-2 1.2a8 8 0 0 0 3.8 3.8l1.2-2L14 10v3a1 1 0 0 1-1 1A11 11 0 0 1 2 3a1 1 0 0 1 1-1z"/></svg>
          416-555-0193
        </li>
        <li>
          <svg viewBox="0 0 16 16" aria-hidden="true"><rect x="4" y="1.5" width="8" height="13" rx="1.5" fill="none" stroke="var(--white)" stroke-width="1.5"/><circle cx="8" cy="12" r="0.9" fill="var(--white)"/></svg>
          416-555-0147
        </li>
        <li>
          <svg viewBox="0 0 16 16" aria-hidden="true"><rect x="1" y="3" width="14" height="10" rx="1" fill="var(--gold)"/><path d="M4 8l3 3 5-6" fill="none" stroke="var(--card)" stroke-width="1.6"/></svg>
          veridax.ca&nbsp; Calvin@veridax.ca
        </li>
      </ul>
    </div>
  </section>
</main>
</body>
</html>
```